Website Design for Horse Blog
Purely Brivelle
Project: Website Design for Horse Blog
Website Design for Horse Blog - Blogging
Creative Brief
Blogging
Brivelle Saddlebreds is a boutique saddlebred horse breeding operation. Purely Brivelle is the name of the blog encouraging older people that it is never too late to start riding horses. It's a feel-good blog intended to attract more people to the Saddlebred Horse Showing industry.
Simple, user-friendly without too much going on. Photography is important.
Modern
Burgundy
Black
Ivory
left side
http://joannevrelstad.example
Most importantly I want to set this website for blogging purposes. The business is just an example of what it is I do. Links to resources will be important for a page. I'm thinking five pages: Blog/Brivelle Saddlebreds/For Sale/Links/Contact Info
crewdalvo crewdalvo
Here is my revised requests: Five pages should be: Home, Blog, Brivelle Saddlebreds, Contact, Links. The title: Purely Brivelle should appear on the Home page along with the Brivelle Saddlebreds logo. I like simple, modern looking pages without a lot of information hitting me from every direction. I have seen very few with black backgrounds, I would like to see more of that.
I think I would like to see the title Purely Brivelle to be displayed with more emphasis as soon as the page loads.

```html
<!DOCTYPE html>
<html lang="en">
<head>
<meta charset="utf-8">
<title>Purely Brivelle — Brivelle Saddlebreds</title>
<link rel="stylesheet" href="https://fonts.googleapis.com/css2?family=Great+Vibes&family=Raleway:wght@400;500;600&display=swap">
<style>
  :root{
    --ivory:#f8f2e2;
    --ivory-light:#fdf9ef;
    --cream-band:#f4ecd2;
    --burgundy:#8a1431;
    --burgundy-dark:#5e0c20;
    --header-rule:#e6bfc6;
    --ink:#2b2326;
    --muted:#7d7374;
    --rule:#e2dbd0;
    --white:#ffffff;
  }
  *{box-sizing:border-box;margin:0;padding:0}
  html,body{width:1200px;height:1104px;overflow:hidden}
  body{background:var(--ivory);font-family:"Raleway",sans-serif;color:var(--ink);position:relative}

  .site-header{position:absolute;left:0;top:0;width:1200px;height:170px;background:var(--ivory-light);
    border-bottom:3px solid var(--header-rule);text-align:center;padding-top:22px}
  .site-title{font-family:"Great Vibes",cursive;font-size:66px;font-weight:400;color:var(--burgundy);line-height:1}
  .brand-name{margin-top:14px;font-size:14px;font-weight:600;letter-spacing:4px;text-transform:uppercase;color:var(--muted)}

  .sidebar{position:absolute;left:100px;top:232px;width:215px;height:560px;box-shadow:0 3px 8px rgba(0,0,0,.25)}
  .panel-title{height:48px;background:linear-gradient(#9d1c3b,var(--burgundy-dark));color:var(--white);
    font-family:"Great Vibes",cursive;font-size:30px;line-height:48px;padding-left:18px;font-weight:400}
  .main-nav{list-style:none;background:var(--white)}
  .main-nav li{height:42px;line-height:42px;padding:0 18px;font-size:14px;color:#555;border-bottom:1px solid var(--rule);
    display:flex;justify-content:space-between}
  .main-nav li::after{content:"›";font-size:20px;color:#666}
  .main-nav li.active{background:var(--burgundy);color:var(--white)}
  .main-nav li.active::after{color:var(--white)}
  .newsletter{background:linear-gradient(var(--burgundy),var(--burgundy-dark));height:212px;padding:18px}
  .field{height:26px;background:var(--white);font-size:12px;color:#666;line-height:26px;padding-left:8px;margin-bottom:10px}
  .subscribe{display:inline-block;background:var(--ivory-light);color:var(--burgundy);font-size:11px;font-weight:600;
    padding:6px 12px;border-radius:3px;letter-spacing:.5px}
  .social{display:flex;gap:8px;margin-top:22px}
  .social span{width:22px;height:22px;border-radius:50%;background:var(--white);opacity:.85}

  .hero{position:absolute;left:315px;top:232px;width:790px;height:540px;
    background:linear-gradient(180deg,#d9dde2 0%,#c4c9c8 35%,#6f7a52 62%,#4f5a35 80%,#3c3a2c 100%)}
  .hero-copy{position:absolute;left:315px;top:540px;width:790px;text-align:center;color:var(--white);
    text-shadow:0 2px 6px rgba(0,0,0,.5)}
  .hero-kicker{font-size:30px;font-weight:400}
  .hero-title{font-family:"Great Vibes",cursive;font-size:64px;line-height:1.1}
  .slider-dots{position:absolute;left:545px;top:688px;display:flex;gap:8px}
  .slider-dots span{width:11px;height:11px;border-radius:50%;background:var(--white)}
  .slider-dots span.on{background:var(--burgundy)}

  .post{position:absolute;left:105px;top:835px;width:1000px;height:180px}
  .post-photo{position:absolute;left:0;top:0;width:168px;height:168px;border-radius:50%;
    background:radial-gradient(circle at 50% 40%,#b7b0a6,#5e6b55);border:6px solid var(--white);
    box-shadow:0 2px 8px rgba(0,0,0,.3)}
  .post-body{position:absolute;left:218px;top:12px;width:782px}
  .post-head{display:flex;align-items:baseline;gap:18px}
  .post-title{font-size:28px;font-weight:500;color:#4a4244}
  .post-date{font-size:12px;color:var(--burgundy)}
  .post-text{margin-top:12px;font-size:12px;line-height:1.75;color:var(--muted)}
  .read-more{color:var(--burgundy)}

  .site-footer{position:absolute;left:0;top:1045px;width:1200px;height:59px;background:var(--cream-band);
    border-top:2px solid #eadfbe;display:flex;justify-content:space-between;align-items:center;padding:0 100px;
    font-size:12px;color:#5c5456}
</style>
</head>
<body>
  <header class="site-header">
    <h1 class="site-title">Purely Brivelle</h1>
    <div class="brand-name">Brivelle Saddlebreds</div>
  </header>

  <aside class="sidebar">
    <div class="panel-title">Menu</div>
    <ul class="main-nav">
      <li class="active">Home</li>
      <li>Blog</li>
      <li>Brivelle Saddlebreds</li>
      <li>For Sale</li>
      <li>Links</li>
      <li>Contact</li>
    </ul>
    <div class="panel-title">News Letter</div>
    <form class="newsletter">
      <div class="field">Name*</div>
      <div class="field">E-mail*</div>
      <span class="subscribe">SUBSCRIBE</span>
      <div class="social"><span></span><span></span><span></span><span></span></div>
    </form>
  </aside>

  <div class="hero" role="img" aria-label="Photo of a smiling woman standing between two chestnut Saddlebred horses in a paddock beside a dark fence"></div>
  <div class="hero-copy">
    <div class="hero-kicker">Encouraging Older People!</div>
    <div class="hero-title">Start Riding Horses...</div>
  </div>
  <div class="slider-dots"><span class="on"></span><span></span><span></span></div>

  <article class="post">
    <div class="post-photo" role="img" aria-label="Round portrait photo of an older rider"></div>
    <div class="post-body">
      <div class="post-head">
        <h2 class="post-title">Encouraging Older People</h2>
        <span class="post-date">23 November 2015</span>
      </div>
      <p class="post-text">Riding is not only for the young. Many of our readers climbed into the saddle for the first time after fifty and found a calm, steady partner in a gentle Saddlebred. In these pages we share their stories, simple lessons for new riders, and honest advice on finding a trainer, a barn and a horse that suits your pace. It is never too late to feel the joy of a first ride around the ring. <span class="read-more">Read More»</span></p>
    </div>
  </article>

  <footer class="site-footer">
    <span>Home &nbsp;/&nbsp; Blog &nbsp;/&nbsp; Brivelle Saddlebreds &nbsp;/&nbsp; For Sale &nbsp;/&nbsp; Links &nbsp;/&nbsp; Contact</span>
    <span>©Brivelle Saddlebreds 2015 | All rights Reserved</span>
  </footer>
</body>
</html>
```